Electrical Contractors Business Card Design

I need a business card design for an electrical contracting business. A theme I was thinking of is the BE of Brightway Electrical both facing each other ie the second E is back to front and maybe each horizontal part of the E's are a different colours of the internal wires of TPS cable. The top would be blue(representing the sky), the middle green(representing the grass) and the lower would be brown(representing below the earth) (neutral,earth and active). And coming out of the back of each E going to each side of the business card would be the white outer sheath of TPS cable. I would like a big part of the card to be a very bright emerald flourescent green and maybe silver for the top half. the message I would like to send is that of an environmentally friendly, ethical business that delivers quality sevice on time.

Target Market(s)

40 to 80 year old home owners

Industry/Entity Type

Electrical

Contact Information for Business Card

Tom Keller
Brightway Electrical
EC 274381
Mob: 0417 592 064

```html
<!DOCTYPE html>
<html lang="en">
<head>
<meta charset="utf-8">
<title>Brightway Electrical – Business Card</title>
<link href="https://fonts.googleapis.com/css2?family=Open+Sans:wght@700;800&display=swap" rel="stylesheet">
<style>
  :root {
    --paper: #ffffff;
    --green-light: #1ba54b;
    --green-dark: #0a5d2a;
    --ring-green: #3fb54a;
    --badge-inner: #0d6b33;
    --badge-core: #138a45;
    --sheath: #ffffff;
    --text: #ffffff;
  }
  html, body {
    margin: 0;
    padding: 0;
    width: 1200px;
    height: 701px;
    overflow: hidden;
    background: var(--paper);
  }
  .card {
    position: relative;
    width: 1200px;
    height: 701px;
    background: var(--paper);
    font-family: "Open Sans", Arial, sans-serif;
    color: var(--text);
  }
  .card__art {
    position: absolute;
    inset: 0;
  }
  .services {
    position: absolute;
    top: 36px;
    left: 0;
    width: 1200px;
    margin: 0;
    padding: 0;
    list-style: none;
    display: flex;
    justify-content: center;
    gap: 22px;
    font-size: 19px;
    font-weight: 800;
    letter-spacing: 0.2px;
  }
  .services li::before {
    content: "";
    display: inline-block;
    width: 11px;
    height: 11px;
    border-radius: 50%;
    background: var(--text);
    margin-right: 16px;
    vertical-align: 2px;
  }
  .badge-text {
    position: absolute;
    left: 374px;
    top: 120px;
    width: 480px;
    height: 480px;
    display: flex;
    flex-direction: column;
    align-items: center;
    justify-content: center;
    text-align: center;
    font-weight: 800;
  }
  .badge-text__owner {
    font-size: 28px;
    letter-spacing: 2px;
    margin: 0 0 6px;
  }
  .badge-text__business {
    font-size: 40px;
    line-height: 1.1;
    letter-spacing: 1px;
    margin: 0 0 22px;
  }
  .badge-text__licence {
    font-size: 26px;
    letter-spacing: 1px;
    margin: 0;
  }
  .mobile {
    position: absolute;
    left: 0;
    top: 610px;
    width: 1200px;
    margin: 0;
    text-align: center;
    font-size: 52px;
    font-weight: 800;
    letter-spacing: 0.5px;
  }
</style>
</head>
<body>
  <main class="card">
    <svg class="card__art" width="1200" height="701" viewBox="0 0 1200 701" aria-hidden="true">
      <defs>
        <radialGradient id="badgeCore" cx="50%" cy="50%" r="50%">
          <stop offset="0%" stop-color="var(--badge-core)"/>
          <stop offset="100%" stop-color="var(--badge-inner)"/>
        </radialGradient>
      </defs>
      <rect class="band-top" x="11" y="11" width="1178" height="679" fill="var(--green-light)"/>
      <path class="band-bottom" d="M11 180 C 250 170 360 250 470 340 L 760 340 C 860 250 960 170 1189 165 L 1189 690 L 11 690 Z" fill="var(--green-dark)"/>
      <path class="cable-sheath" d="M11 174 C 250 164 360 244 470 334 M760 334 C 860 244 960 164 1189 159" fill="none" stroke="var(--sheath)" stroke-width="12"/>
      <circle class="badge" cx="614" cy="360" r="222" fill="url(#badgeCore)" stroke="var(--ring-green)" stroke-width="40"/>
    </svg>

    <ul class="services">
      <li>ELECTRICAL WIRING &amp; CONSTRUCTION</li>
      <li>COMMERCIAL LIGHTING</li>
      <li>ADD CUSTOMER HIGHLIGHT</li>
    </ul>

    <div class="badge-text">
      <p class="badge-text__owner">TOM KELLER</p>
      <p class="badge-text__business">BRIGHTWAY<br>ELECTRICAL</p>
      <p class="badge-text__licence">LICENCE # EC 274381</p>
    </div>

    <p class="mobile">MOBILE # 0417 592 064</p>
  </main>
</body>
</html>
```